political campaign tax exemption on school taxes that dont have kids in the district

Harlow Vale School Board Races

Taxes, Taxes, Taxes!
Everyone pays them!
You have tax exemption for the elderly.
You have tax exemption for the veterans.
What about tax exemptions for you?

In Texas, a governing entity, has the option of giving a 20 percent tax exemption. Our current school board, hasnt offered it you! We will!

Can we count on your vote? You can count on ours!
small discloure (political ad paid by candidates)

attached are the candidates for this exemption

Political

• need to include disclaimer at bottom.

political ad paid by candidate

```html
<!DOCTYPE html>
<html lang="en">
<head>
<meta charset="utf-8">
<title>Harlow Vale School Board Races – Tax Exemption Postcard</title>
<link href="https://fonts.googleapis.com/css2?family=Bebas+Neue&family=Roboto+Condensed:wght@400;700&display=swap" rel="stylesheet">
<style>
  :root{
    --page:#ffffff;
    --charcoal:#262626;
    --charcoal-2:#333333;
    --orange:#ee6a2c;
    --orange-dark:#a8431a;
    --blue:#1fa3d4;
    --blue-dark:#12708f;
    --panel:#e7e5e2;
    --ink:#3a3a3a;
    --white:#ffffff;
    --muted:#cfcfcf;
    --navy:#1f2a6b;
    --gold:#e9b52a;
    --red:#c8262c;
    --line:#222222;
  }
  *{box-sizing:border-box;margin:0;padding:0}
  html,body{width:925px;height:1200px;overflow:hidden;background:var(--page)}
  body{position:relative;font-family:"Bebas Neue",sans-serif}

  .postcard{position:absolute;left:150px;width:620px;height:480px;overflow:hidden}
  .postcard--front{top:50px;background:var(--charcoal)}
  .postcard--back{top:630px;background:var(--white);border:1px solid #d8d8d8}

  .shapes{position:absolute;inset:0}

  .banner{position:absolute;color:var(--white);letter-spacing:.5px;line-height:1}
  .banner--orange{background:var(--orange)}
  .banner--blue{background:var(--blue)}

  /* front */
  .front-headline{left:16px;top:43px;width:374px;height:64px;font-size:45px;padding:10px 0 0 24px}
  .front-subline{left:36px;top:358px;width:280px;height:50px;font-size:32px;color:var(--charcoal);padding:10px 0 0 12px}
  .elderly-claim{position:absolute;right:20px;top:282px;text-align:right;color:var(--white);line-height:1}
  .elderly-claim span{display:block;font-size:40px;margin-bottom:2px}
  .elderly-claim strong{display:block;font-weight:400;font-size:68px;margin-top:4px}
  .veterans-claim{position:absolute;left:20px;top:456px;color:var(--white);font-size:17px;letter-spacing:.5px;line-height:1}

  /* back */
  .back-headline{left:93px;top:5px;width:253px;height:62px;font-size:27px;text-align:right;padding:6px 12px 0 0;line-height:.95}
  .back-body{position:absolute;left:14px;top:82px;width:294px;text-align:center;font-family:"Roboto Condensed",sans-serif;font-weight:700;font-size:14.5px;line-height:1.2;color:var(--ink)}
  .promise{position:absolute;left:0;top:140px;width:308px;text-align:center;font-family:"Roboto Condensed",sans-serif;font-weight:700;font-size:36px;line-height:1;color:var(--orange)}
  .back-question{left:38px;top:192px;width:303px;height:43px;font-size:29px;text-align:center;padding-top:7px}
  .back-answer{position:absolute;left:0;top:252px;width:308px;text-align:center;font-size:32px;color:var(--orange)}

  .candidates{position:absolute;left:16px;top:355px;display:flex;gap:7px}
  .candidate{width:85px;height:84px;padding:6px 4px;display:flex;flex-direction:column;justify-content:center;align-items:center;text-align:center;line-height:1;overflow:hidden}
  .candidate b{font-weight:400;font-size:19px}
  .candidate small{font-family:"Roboto Condensed",sans-serif;font-size:7.5px;margin-top:4px;line-height:1.15}
  .candidate--one{background:var(--navy);color:var(--white)}
  .candidate--two{background:var(--gold);color:var(--navy)}
  .candidate--three{background:var(--white);color:var(--red)}
  .candidate--three b{font-size:14px;white-space:nowrap}
  .candidate--three small{margin:3px 0 5px}
  .disclaimer{position:absolute;left:16px;top:452px;width:276px;font-family:"Roboto Condensed",sans-serif;font-size:9px;color:var(--muted);line-height:1}

  .stamp-box{position:absolute;left:543px;top:50px;width:50px;height:60px;border:1px solid var(--line)}
  .address-line{position:absolute;left:415px;width:178px;height:1px;background:var(--line)}
</style>
</head>
<body>

<section class="postcard postcard--front" aria-label="Postcard front">
  <svg class="shapes" viewBox="0 0 620 480" width="620" height="480">
    <defs>
      <linearGradient id="coinsTones" x1="0" y1="0" x2="1" y2="1">
        <stop offset="0" stop-color="#3c3d42"/>
        <stop offset=".45" stop-color="#c9cdd2"/>
        <stop offset=".75" stop-color="#eef0f2"/>
        <stop offset="1" stop-color="#b7b2a6"/>
      </linearGradient>
    </defs>
    <polygon points="0,0 620,0 620,255 0,440" fill="url(#coinsTones)" role="img" aria-label="Photo of a hand stacking coins into rising piles on a desk"/>
    <polygon points="0,440 620,255 620,262 0,450" fill="var(--white)"/>
  </svg>
  <div class="banner banner--orange front-headline">Taxes, Taxes, Taxes!</div>
  <div class="banner banner--blue front-subline">Everyone pays them!</div>
  <p class="elderly-claim"><span>You</span><span>have tax</span><span>exemption for</span><strong>The Elderly</strong></p>
  <p class="veterans-claim">You have tax exemption for the veterans</p>
</section>

<section class="postcard postcard--back" aria-label="Postcard back">
  <svg class="shapes" viewBox="0 0 620 480" width="620" height="480">
    <rect x="0" y="0" width="308" height="480" fill="var(--panel)"/>
    <polygon points="0,292 308,352 308,480 0,480" fill="var(--charcoal-2)"/>
    <polygon points="334,67 346,67 334,78" fill="var(--orange-dark)"/>
    <polygon points="38,235 50,235 38,246" fill="var(--blue-dark)"/>
  </svg>
  <div class="banner banner--orange back-headline">What about tax<br>exemptions for you?</div>
  <p class="back-body">In Texas, a governing entity, has the option of giving a 20 percent tax exemption. Our current school board, hasnt offered it you!</p>
  <p class="promise">We will!</p>
  <div class="banner banner--blue back-question">Can we count on your vote?</div>
  <p class="back-answer">You can count on ours!</p>

  <div class="candidates" aria-label="Candidates">
    <div class="candidate candidate--one"><b>Marco Ellery</b><small>Harlow Vale School Board Pl. 1</small></div>
    <div class="candidate candidate--two"><b>Tomas Brandt</b><small>Harlow Vale ISD School Board Pl. 5</small></div>
    <div class="candidate candidate--three"><b>Dean Whitford</b><small>Harlow Vale ISD Pl. 3</small><b>Nico Ardent</b></div>
  </div>
  <p class="disclaimer">Political ad paid for by the candidates</p>

  <div class="stamp-box" aria-label="Stamp box"></div>
  <div class="address-line" style="top:236px"></div>
  <div class="address-line" style="top:273px"></div>
  <div class="address-line" style="top:311px"></div>
</section>

</body>
</html>
```